Brix2Key Header

I want a professional Letterhead for my law firm. I'm attaching the letterhead I currently use in Word and PDF form. I'm also attaching my logo, and an example header that I like.

```html
<!DOCTYPE html>
<html lang="en">
<head>
<meta charset="utf-8">
<title>Brix2Key Letterhead</title>
<link href="https://fonts.googleapis.com/css2?family=Montserrat:wght@400;600;700;800&family=Open+Sans:wght@400;600&display=swap" rel="stylesheet">
<style>
  :root {
    --ink: #111111;
    --text: #3a3a3a;
    --muted: #6d6d6d;
    --teal: #2cc3c7;
    --paper: #ffffff;
    --band: #141414;
  }
  * { box-sizing: border-box; margin: 0; padding: 0; }
  html, body { width: 857px; height: 1200px; overflow: hidden; background: var(--paper); }
  .letterhead {
    position: relative; width: 857px; height: 1200px;
    font-family: "Open Sans", Arial, sans-serif; color: var(--text);
  }
  .brand-block { position: absolute; left: 0; top: 0; width: 330px; height: 90px; }
  .brand-name {
    position: absolute; left: 42px; top: 26px;
    font-family: "Montserrat", Arial, sans-serif; font-weight: 800;
    font-size: 30px; letter-spacing: 1px; color: var(--paper);
    display: flex; align-items: center; gap: 10px;
  }
  .brand-dot { width: 12px; height: 12px; border-radius: 50%; background: var(--teal); }
  .firm-contact {
    position: absolute; right: 40px; top: 16px; text-align: right;
    font-family: "Montserrat", Arial, sans-serif; color: var(--ink);
  }
  .firm-title { font-weight: 800; font-size: 14px; margin-bottom: 14px; }
  .firm-line { font-size: 11px; font-weight: 600; line-height: 16px; }
  .accent-rule { position: absolute; left: 40px; right: 40px; top: 190px; height: 1px; background: #d8d8d8; }
  .recipient { position: absolute; left: 40px; top: 286px; font-size: 9.5px; line-height: 14px; }
  .recipient .label { font-weight: 700; color: var(--ink); margin-bottom: 6px; }
  .recipient .name { font-weight: 600; color: var(--ink); }
  .date { position: absolute; right: 40px; top: 428px; font-size: 9.5px; font-weight: 700; color: var(--ink); }
  .letter-body { position: absolute; left: 40px; right: 40px; top: 480px; font-size: 9.5px; line-height: 15px; }
  .letter-body p { margin-bottom: 14px; }
  .letter-body ul { margin: 0 0 30px 40px; }
  .letter-body li { margin-bottom: 3px; }
  .sign-off { position: absolute; left: 40px; top: 992px; font-size: 9.5px; line-height: 14px; }
  .signature { width: 70px; height: 32px; margin: 6px 0 4px; border-radius: 4px;
    background: linear-gradient(90deg, #d9e2ec, #eef2f6); }
  .sign-off .name { font-weight: 700; color: var(--ink); }
  .sign-off .role { font-style: italic; color: var(--muted); }
  .footer { position: absolute; left: 0; bottom: 0; width: 857px; height: 92px; background: var(--band); }
  .footer-stripe { position: absolute; left: 0; top: -4px; width: 857px; height: 4px; background: var(--teal); }
  .footer-cols {
    position: absolute; left: 112px; right: 50px; top: 30px;
    display: flex; justify-content: space-between;
    font-family: "Montserrat", Arial, sans-serif; color: var(--paper);
    font-size: 10px; font-weight: 600; line-height: 16px;
  }
</style>
</head>
<body>
<div class="letterhead">
  <div class="brand-block">
    <svg width="330" height="90" viewBox="0 0 330 90" aria-hidden="true">
      <polygon points="0,0 330,0 290,90 0,90" fill="#141414"/>
      <polygon points="290,90 330,0 336,0 296,90" fill="#2cc3c7"/>
    </svg>
    <div class="brand-name"><span>BRIX2KEY</span><span class="brand-dot"></span></div>
  </div>

  <div class="firm-contact">
    <div class="firm-title">MATEO R. ALVAREZ, ATTORNEY AT LAW, PLLC</div>
    <div class="firm-line">2450 CARVER STREET SUITE 300</div>
    <div class="firm-line">AUSTIN, TEXAS 78701</div>
    <div class="firm-line">TELEPHONE: (555) 210-4830</div>
    <div class="firm-line">FAX: (555) 210-4831</div>
    <div class="firm-line">INFO@BRIX2KEY.COM</div>
    <div class="firm-line">WWW.BRIX2KEY.COM</div>
  </div>

  <div class="accent-rule"></div>

  <div class="recipient">
    <div class="label">TO</div>
    <div class="name">Dana Whitfield</div>
    <div>Position / Company Name</div>
    <div style="margin-top:8px">28th Street Name, City Name</div>
    <div>Location Name,ES</div>
  </div>

  <div class="date">DATE : 11 JULY 2021</div>

  <div class="letter-body">
    <p>Dear Sir</p>
    <p>There are many variations of passages of Lorem Ipsum available, but the majority have suffered alteration in some form, by injected humour. But I must explain to you how all this mistaken idea of denouncing pleasure and praising pain was born and I will give you a complete account of the system, and expound the actual teachings of the great explorer of the truth, the master-builder of human happiness. No one rejects, dislikes, or avoids pleasure itself, because it is pleasure, but because those who do not know how to pursue pleasure rationally encounter consequences that are extremely painful. Nor again is there anyone who loves or pursues or desires to obtain pain of itself, because it is pain, but because occasionally circumstances occur in which toil and pain can procure him some great pleasure. To take a trivial example, which of us ever undertakes</p>
    <ul>
      <li>Nunc rhoncus quam ac sapien pulvinar, vitae convallis mi porttitor.</li>
      <li>Phasellus placerat tortor maximus, faucibus magna nec, consectetur nisi.</li>
      <li>Variations of passages of Lorem Ipsum available, but</li>
    </ul>
    <p>There are many variations of passages of Lorem Ipsum available, but the majority have suffered alteration in some form, by injected humour. But I must explain to you how all this mistaken idea of denouncing pleasure and praising pain was born and I will give you a complete account of the system, and expound the actual teachings of the great explorer of the truth, the master-builder of human happiness. No one rejects, dislikes, or avoids pleasure itself, because it is pleasure, but because those who do not know how to pursue pleasure rationally encounter consequences that are extremely painful.</p>
    <p>Nor again is there anyone who loves or pursues or desires to obtain pain of itself, because it is pain, but because occasionally circumstances occur in which toil and pain can procure him some great pleasure. To take a trivial example, which of us ever undertakes</p>
  </div>

  <div class="sign-off">
    <div>Sincerely</div>
    <div class="signature" role="img" aria-label="Handwritten signature"></div>
    <div class="name">Mateo R. Alvarez</div>
    <div class="role">Attorney at Law</div>
  </div>

  <div class="footer">
    <div class="footer-stripe"></div>
    <div class="footer-cols">
      <div>2450 CARVER STREET SUITE 300<br>AUSTIN, TEXAS 78701</div>
      <div>INFO@BRIX2KEY.COM<br>WWW.BRIX2KEY.COM</div>
      <div>TELEPHONE: (555) 210-4830<br>FAX: (555) 210-4831</div>
    </div>
  </div>
</div>
</body>
</html>
```